Fresh, modern, fun business card for pediatric dental practice

Need a business card for fresh, modern, fun pediatric dental practice

Clean look that matches our website's font and colors

We prefer the look of curved corners on business cards

Target Market(s)

parents (mothers) of young children, professionals, mid-high class

Industry/Entity Type

Dental

Contact Information for Business Card

Maplewood Pediatric Dentistry
482 Corbett Lane
Suite 619
Fernbrook, ST 00000
555.555.0193
www.maplewoodtotsdental.example

Mei-Hua Tran, DMD
Colette Margrave, DMD
(we are working on our email address, but we would like that on the card as well)

Font styles to use
Sans Serif

Requirements
Must have
• All info; we would also like to make cards for individual staff members
• colors from our website and color palatte, attatched
• use same font and design as website for branding
Nice to have
• clean, simple card that has a pop of color
• we would like to see a few designs with our tag line "where smiles get brighter"
• we are not sure if we want to have it on there or not
• we would like to see a few designs incorporating the ribbon graphic on our website where the word WELCOME is

```html
<!DOCTYPE html>
<html lang="en">
<head>
<meta charset="utf-8">
<title>Maplewood Pediatric Dentistry – Business Card</title>
<link href="https://fonts.googleapis.com/css2?family=Questrial&family=Nunito+Sans:wght@700;800&display=swap" rel="stylesheet">
<style>
  :root {
    --plum: #4e2352;
    --plum-light: #5d2d60;
    --sun: #f8b92a;
    --sun-soft: rgba(248, 185, 42, 0.35);
    --white: #ffffff;
    --backdrop: #e9e6ea;
  }
  * { box-sizing: border-box; margin: 0; padding: 0; }
  html, body { width: 1200px; height: 930px; overflow: hidden; }
  body {
    background: var(--backdrop);
    font-family: "Questrial", "Century Gothic", sans-serif;
    position: relative;
  }
  .card {
    position: absolute;
    left: 250px;
    width: 700px;
    height: 400px;
    border-radius: 24px;
    background: linear-gradient(135deg, var(--plum-light), var(--plum));
    color: var(--white);
    overflow: hidden;
  }
  .card--front { top: 45px; }
  .card--back { top: 485px; }

  /* front */
  .front-brand {
    position: absolute;
    left: 0; right: 0; top: 150px;
    display: flex; justify-content: center; align-items: center; gap: 18px;
  }
  .brand-dot {
    width: 34px; height: 34px; border-radius: 50%;
    background: var(--sun);
  }
  .brand-name {
    font-family: "Questrial", sans-serif;
    color: var(--sun);
    font-size: 40px;
    letter-spacing: 0.5px;
    white-space: nowrap;
  }
  .front-web {
    position: absolute;
    left: 0; right: 0; bottom: 62px;
    text-align: center;
    font-size: 17px;
    letter-spacing: 1px;
    color: var(--white);
  }

  /* back */
  .back-info {
    position: absolute;
    left: 44px; top: 40px;
    width: 420px;
  }
  .back-info .brand-name { font-size: 27px; display: block; }
  .doctor {
    font-family: "Nunito Sans", sans-serif;
    font-weight: 800;
    font-size: 28px;
    margin-top: 20px;
  }
  .contacts { list-style: none; margin-top: 16px; }
  .contacts li {
    display: flex; align-items: center; gap: 12px;
    font-size: 18px; line-height: 30px;
  }
  .icon { width: 22px; height: 22px; flex: none; }
  .practice-heading {
    margin-top: 18px;
    font-family: "Nunito Sans", sans-serif;
    font-weight: 700;
    font-size: 15px;
    letter-spacing: 1px;
    text-transform: uppercase;
    color: var(--sun);
  }
  .address { font-size: 17px; line-height: 23px; margin-top: 4px; font-style: normal; }
  .emblem-area {
    position: absolute;
    right: 60px; top: 70px;
    width: 240px; height: 240px;
    border-radius: 50%;
    background: radial-gradient(circle, var(--sun-soft), rgba(248, 185, 42, 0) 70%);
  }
</style>
</head>
<body>

<section class="card card--front" aria-label="Card front">
  <div class="front-brand">
    <span class="brand-dot"></span>
    <span class="brand-name">Maplewood Pediatric Dentistry</span>
  </div>
  <p class="front-web">www.maplewoodtotsdental.example</p>
</section>

<section class="card card--back" aria-label="Card back">
  <div class="back-info">
    <span class="brand-name">Maplewood Pediatric Dentistry</span>
    <p class="doctor">Mei-Hua Tran, DMD</p>
    <ul class="contacts">
      <li>
        <svg class="icon" viewBox="0 0 24 24" fill="none" stroke="#f8b92a" stroke-width="1.8"><circle cx="12" cy="12" r="10.5"/><path d="M8.5 7.5c.6-.6 1.3-.5 1.7.1l1 1.5c.3.5.2 1-.2 1.4l-.6.6c.5 1.2 1.4 2.1 2.6 2.6l.6-.6c.4-.4.9-.5 1.4-.2l1.5 1c.6.4.7 1.1.1 1.7l-.6.6c-.8.8-2.3.6-4.2-.8-1.3-1-2.3-2-3.3-3.3-1.4-1.9-1.6-3.4-.8-4.2z" fill="#f8b92a" stroke="none"/></svg>
        555.555.0193
      </li>
      <li>
        <svg class="icon" viewBox="0 0 24 24" fill="none" stroke="#f8b92a" stroke-width="1.8"><circle cx="12" cy="12" r="10.5"/><rect x="7" y="8.5" width="10" height="7" rx="1"/><path d="M7 9l5 4 5-4"/></svg>
        info@maplewoodtotsdental.example
      </li>
      <li>
        <svg class="icon" viewBox="0 0 24 24" fill="none" stroke="#f8b92a" stroke-width="1.8"><circle cx="12" cy="12" r="10.5"/><circle cx="12" cy="12" r="5"/><path d="M7 12h10M12 7c-2 3-2 7 0 10M12 7c2 3 2 7 0 10"/></svg>
        www.maplewoodtotsdental.example
      </li>
    </ul>
    <p class="practice-heading">Maplewood Pediatric Dentistry</p>
    <address class="address">
      Maplewood Pediatric Dentistry<br>
      482 Corbett Lane<br>
      Suite 619, Fernbrook, ST 00000
    </address>
  </div>
  <div class="emblem-area" role="img" aria-label="Area for the practice's large decorative emblem"></div>
</section>

</body>
</html>
```